Brush up bramtide landing page projects.

Hello, we are organizing the bram-tide website.

http://www.bram-tide.jp

We are looking for a designer and need to brush up this landing page.
You don't need to worry about Japanese. Feel free to design the site in English.

http://www.bram-tide.jp/lp_c.html

please contact me.
Thank you.

```html
<!DOCTYPE html>
<html lang="ja">
<head>
<meta charset="utf-8">
<title>bramtide</title>
<link href="https://fonts.googleapis.com/css2?family=Noto+Sans+JP:wght@400;500;700&family=Open+Sans:wght@400;600&display=swap" rel="stylesheet">
<style>
:root{
  --teal:#00a0a0;
  --teal-dark:#008c8c;
  --pink:#e4267f;
  --ink:#333;
  --grey:#777;
  --line:#e2e2e2;
  --panel:#f4f4f4;
  --footer-dark:#333;
  --white:#fff;
}
*{box-sizing:border-box;margin:0;padding:0}
html,body{width:1200px;height:1199px;overflow:hidden;background:var(--white)}
body{font-family:"Open Sans","Noto Sans JP",sans-serif;color:var(--ink);position:relative}
.abs{position:absolute}
a{color:inherit;text-decoration:none}
h2,h3,h4{font-weight:400}

/* top utility bar */
.utility{top:0;left:0;width:1200px;height:18px;border-top:2px solid var(--teal)}
.utility-links{right:250px;top:4px;font-size:7px;color:var(--pink);display:flex;gap:0}
.utility-links span{padding:0 14px;border-left:1px solid #ccc}
.utility-links span:first-child{border-left:0}
.utility-social{right:220px;top:5px;display:flex;gap:8px}
.utility-social i{display:block;width:7px;height:7px;background:var(--teal);border-radius:50%}

/* header */
.header{top:18px;left:0;width:1200px;height:66px;background:var(--teal)}
.brand{left:286px;top:23px;font-size:19px;font-weight:600;color:var(--white);letter-spacing:.5px;display:flex;align-items:center;gap:6px}
.brand i{display:block;width:9px;height:9px;background:var(--white);border-radius:50%}
.nav{left:404px;top:0;display:flex;height:66px}
.nav-item{width:63px;height:66px;display:flex;flex-direction:column;align-items:center;justify-content:center;gap:8px;color:var(--white);font-size:6.5px;font-family:"Noto Sans JP",sans-serif;white-space:nowrap}
.nav-item+.nav-item{margin-left:2px;width:76px}
.nav-item.is-active{background:var(--pink);width:63px}
.nav-item svg{width:26px;height:22px}
.hotline{right:200px;top:8px;color:var(--white);text-align:right;font-family:"Noto Sans JP",sans-serif}
.hotline small{display:block;font-size:8px}
.hotline strong{display:flex;align-items:center;gap:4px;font-size:18px;font-weight:500;font-family:"Open Sans",sans-serif;justify-content:flex-end}
.hotline em{display:block;font-style:normal;font-size:6.5px}

/* area bar */
.areabar{top:84px;left:0;width:1200px;height:22px;border-bottom:1px solid var(--line)}
.area-label{left:286px;top:5px;font-size:7.5px;color:var(--grey);display:flex;align-items:center;gap:5px;font-family:"Noto Sans JP",sans-serif}
.area-list{left:404px;top:5px;display:flex;gap:13px;font-size:7.5px;color:var(--teal);font-family:"Noto Sans JP",sans-serif}

.tagline{right:259px;top:116px;font-size:14px;color:var(--teal);font-family:"Noto Sans JP",sans-serif}
.tagline b{font-weight:400;color:var(--pink)}

/* sidebar */
.side{left:286px;top:150px;width:152px}
.side-photo{position:absolute;left:0;top:8px;width:70px;height:76px;background:linear-gradient(180deg,#e9ddd6,#c9b9ad)}
.side-bubble{position:absolute;left:72px;top:8px;width:80px;height:40px;border-radius:50%;background:#eee;font-size:6px;color:var(--teal);display:flex;align-items:center;justify-content:center;text-align:center;line-height:1.4}
.quote-btn{position:absolute;left:0;top:84px;width:152px;height:36px;background:var(--pink);color:var(--white);font-size:13px;font-family:"Noto Sans JP",sans-serif;display:flex;align-items:center;padding-left:8px;gap:14px}
.side-title{position:absolute;left:0;top:132px;width:152px;font-size:10px;color:#555;border-bottom:1px solid var(--line);padding-bottom:5px}
.side-text{position:absolute;left:0;top:162px;width:152px;font-size:6.5px;line-height:1.7;color:#555}
.side-menu{position:absolute;left:0;top:212px;width:152px;list-style:none;font-size:7.5px}
.side-menu li{height:24.5px;line-height:24.5px;border-bottom:1px solid var(--line);color:var(--teal)}
.side-menu li.sub{padding-left:20px;color:#666}
.side-menu li.hot{color:var(--pink)}
.side-card{position:absolute;left:0;width:152px;border:1px solid var(--line);border-radius:2px}
.card-feature{top:373px;height:130px}
.card-feature .visual{position:absolute;left:6px;top:12px;width:138px;height:66px;background:linear-gradient(90deg,#d8c6bb,#9fd6d4,#d8c6bb)}
.card-feature p{position:absolute;left:6px;top:92px;width:138px;font-size:6px;line-height:1.6;color:#555}
.card-mini{top:516px;height:38px;display:flex;align-items:center;gap:14px;padding-left:6px;font-size:10px;color:#555;white-space:nowrap}
.card-mini .icon{width:22px;height:24px;background:linear-gradient(180deg,#f1d9c9,#e8a06b);border-radius:3px}
.card-partner{top:568px;height:60px;display:flex;flex-direction:column;align-items:center;justify-content:center;gap:4px}
.card-partner b{display:flex;align-items:center;gap:5px;font-size:16px;font-weight:600;color:#444}
.card-partner b i{display:block;width:10px;height:10px;border-radius:50%;background:#444}
.card-partner small{font-size:5.5px;color:#666;font-family:"Noto Sans JP",sans-serif}

/* hero */
.hero{left:445px;top:142px;width:496px;height:218px;border:3px solid var(--teal);background:var(--white);overflow:hidden;font-family:"Noto Sans JP",sans-serif}
.hero-photo{position:absolute;right:0;top:0;width:210px;height:212px;background:radial-gradient(circle at 55% 45%,#d9bda9 0,#c2a08a 25%,#7fc3c4 55%,#f1f1f1 75%)}
.hero-title{position:absolute;left:6px;top:16px;font-size:18px;font-weight:700;color:var(--teal);line-height:1.1}
.hero-title small{font-size:15px}
.hero-truck{position:absolute;left:222px;top:26px;width:56px;height:22px;background:var(--teal);color:var(--white);font-size:6px;display:flex;align-items:center;justify-content:center}
.hero-rule{position:absolute;left:6px;top:70px;width:272px;border-top:1px dashed var(--teal)}
.hero-badge{position:absolute;left:20px;top:88px;width:80px;height:80px;border-radius:50%;background:var(--pink);color:var(--white);font-size:10px;display:flex;align-items:center;justify-content:center;text-align:center;line-height:1.4}
.hero-role{position:absolute;left:108px;top:92px;font-size:14px;color:var(--teal);font-weight:500;line-height:1.25}
.hero-kana{position:absolute;left:125px;top:134px;font-size:7px;color:var(--teal);letter-spacing:14px}
.hero-name{position:absolute;left:108px;top:144px;font-size:28px;color:var(--teal);font-weight:500;letter-spacing:8px}
.hero-bubble{position:absolute;right:22px;top:8px;width:102px;height:112px;border-radius:50%;border:2px solid var(--teal);background:var(--white);font-size:8px;font-weight:700;line-height:1.5;text-align:center;display:flex;align-items:center;justify-content:center;white-space:nowrap}
.hero-bubble b{color:var(--pink)}
.hero-arrow{position:absolute;top:92px;width:22px;height:34px;background:var(--teal);display:flex;align-items:center;justify-content:center}
.hero-arrow.prev{left:0}.hero-arrow.next{right:0}
.hero-dots{position:absolute;left:224px;top:200px;display:flex;gap:4px}
.hero-dots i{display:block;width:7px;height:7px;background:#bbb}
.hero-dots i:first-child{background:var(--pink)}
.hero-dots i:nth-child(2){background:var(--teal)}

/* ads */
.ad-heading{left:445px;top:376px;font-size:13px;color:var(--teal)}
.ad{left:445px;width:496px;border:1px solid var(--line);padding:2px}
.ad-inner{width:100%;height:100%;position:relative;overflow:hidden;font-family:"Noto Sans JP",sans-serif}
.ad-discount{top:405px;height:66px}
.ad-discount .ad-inner{background:var(--pink);color:var(--white);font-size:25px;font-weight:700;display:flex;align-items:center;padding-left:10px}
.ad-discount .people{position:absolute;right:0;top:0;width:90px;height:100%;background:linear-gradient(90deg,#e4267f,#c7a18a)}
.ad-press{top:475px;height:84px}
.ad-press .ad-inner{background:#eee}
.ad-press .mag{position:absolute;left:0;top:0;width:100px;height:100%;background:linear-gradient(135deg,#e7a0a0,#f6d77a,#9ad)}
.ad-press .ribbon{position:absolute;left:100px;top:8px;width:350px;height:62px;background:#f6d54d;font-size:14px;font-weight:700;text-align:center;padding-top:8px;line-height:1.5}
.ad-press .ribbon b{color:var(--pink)}
.ad-press .ribbon em{font-style:normal;color:var(--teal);font-size:18px}
.ad-art{top:564px;height:75px}
.ad-art .ad-inner{background:linear-gradient(90deg,#6b5a4a,#8a7a62,#4f4538)}
.ad-art .copy{position:absolute;left:0;top:0;width:160px;height:100%;background:var(--teal);color:var(--white);padding:8px 6px}
.ad-art .copy b{display:block;font-size:15px;line-height:1.3}
.ad-art .copy small{display:block;font-size:5px;margin-top:6px;line-height:1.4}

/* news */
.news{top:658px;width:230px;font-size:7px}
.news h3{font-size:7.5px;font-weight:500;font-family:"Noto Sans JP",sans-serif;margin-bottom:18px}
.news-item{font-size:6.2px;line-height:1.5;color:#555;margin-bottom:11px}
.news-item a{color:var(--teal)}
.news-item strong{display:block;font-weight:400;color:var(--teal);font-size:8.5px}
.news-left{left:445px}
.news-right{left:711px}
.news-divider{left:445px;top:780px;width:496px;border-top:1px solid var(--line)}

/* social row */
.fb{left:286px;top:792px;width:152px;height:154px;border:1px solid var(--line)}
.fb h3{height:28px;background:var(--teal);color:var(--white);font-size:12px;font-weight:400;padding:6px 7px}
.fb .mini-brand{margin:8px 7px;font-size:7px;color:var(--teal);font-weight:600}
.tweets{left:445px;top:792px;width:248px;height:154px;background:var(--white)}
.tweets h3{height:28px;background:var(--panel);font-size:12px;font-weight:400;color:var(--teal);display:flex;align-items:center;gap:6px;padding-left:8px}
.tweets h3 i{display:block;width:14px;height:14px;border-radius:50%;background:var(--teal)}
.tweet{display:flex;gap:6px;padding:8px;height:62px}
.tweet.alt{background:var(--panel)}
.tweet .mini-brand{font-size:6px;font-weight:600;color:var(--teal);width:28px;padding-top:2px}
.tweet p{font-size:6px;line-height:1.45;color:#444;width:196px}
.tweet p a{color:var(--teal)}
.tweet p small{display:block;color:#999;font-size:5.5px;margin-top:8px}
.contact{left:711px;top:792px;width:230px;height:154px;border:1px solid var(--line)}
.contact h3{position:absolute;left:6px;top:8px;font-size:13px;font-weight:400;color:var(--teal)}
.contact .btn{position:absolute;top:42px;width:104px;height:24px;background:var(--pink);color:var(--white);font-size:9.5px;display:flex;align-items:center;padding-left:10px;gap:30px}
.contact .btn.one{left:6px}.contact .btn.two{left:120px}
.contact .tel{position:absolute;left:6px;top:80px;display:flex;align-items:center;gap:6px;font-size:27px;line-height:1;color:var(--teal);white-space:nowrap}
.contact .hours{position:absolute;left:10px;top:122px;font-size:10px;color:var(--teal);letter-spacing:.6px;white-space:nowrap}

/* footer */
.footer{top:985px;left:0;width:1200px;height:171px;background:var(--teal);color:var(--white)}
.foot-col{position:absolute;top:26px;width:162px}
.foot-col h4{font-size:13px;font-weight:400;padding-bottom:12px;border-bottom:1px solid rgba(255,255,255,.2);margin-bottom:10px}
.foot-col li{list-style:none;font-size:10px;line-height:16.5px}
.copyright{top:1156px;left:0;width:1200px;height:43px;background:var(--footer-dark);color:#aaa;font-size:6.5px}
.copyright .left{position:absolute;left:286px;top:18px;display:flex;gap:8px;align-items:center}
.copyright .left b{color:var(--teal);font-size:7px}
.copyright .right{position:absolute;right:259px;top:18px}
</style>
</head>
<body>

<div class="abs utility">
  <div class="abs utility-links"><span>Lorem Ipsum</span><span>Lorem Ipsum</span><span>Lorem Ipsum</span></div>
  <div class="abs utility-social"><i></i><i></i></div>
</div>

<header class="abs header">
  <div class="abs brand"><i></i>bramtide</div>
  <nav class="abs nav">
    <a class="nav-item is-active"><svg viewBox="0 0 26 22"><rect x="5" y="4" width="16" height="14" fill="none" stroke="#fff" stroke-width="1.5"/></svg>お片づけ</a>
    <a class="nav-item"><svg viewBox="0 0 26 22"><path d="M6 7l7-4 7 4v9l-7 4-7-4z" fill="none" stroke="#fff" stroke-width="1.5"/></svg>お預かり</a>
    <a class="nav-item"><svg viewBox="0 0 26 22"><rect x="3" y="8" width="20" height="9" fill="none" stroke="#fff" stroke-width="1.5"/></svg>ブラム回収・買取</a>
    <a class="nav-item"><svg viewBox="0 0 26 22"><rect x="6" y="5" width="14" height="12" fill="none" stroke="#fff" stroke-width="1.5"/></svg>ブラムオク</a>
    <a class="nav-item"><svg viewBox="0 0 26 22"><path d="M4 16h18M7 16V7h12v9" fill="none" stroke="#fff" stroke-width="1.5"/></svg>リサイクルショップ</a>
  </nav>
  <div class="abs hotline">
    <small>Lorem Ipsum</small>
    <strong><svg width="14" height="14" viewBox="0 0 14 14"><circle cx="7" cy="7" r="6" fill="none" stroke="#fff" stroke-width="1.3"/><path d="M5 4l1 2-1 1 2 2 1-1 2 1-1 2c-3 0-6-3-6-6z" fill="#fff"/></svg>0120-418-627</strong>
    <em>平日 9:00〜22:00 / 日祝 9:00〜20:00</em>
  </div>
</header>

<div class="abs areabar">
  <div class="abs area-label"><svg width="7" height="9" viewBox="0 0 7 9"><path d="M3.5 9L1 4.5A2.5 2.5 0 1 1 6 4.5z" fill="#999"/></svg>対応エリア</div>
  <div class="abs area-list"><span>埼玉県</span><span>千葉県</span><span>東京都</span><span>神奈川県</span><span>静岡県</span><span>大阪府</span><span>兵庫県</span></div>
</div>

<p class="abs tagline">そんなにいらない、Less is <b>Beautiful.</b></p>

<aside class="abs side">
  <div class="side-photo" role="img" aria-label="Photo of a woman using a smartphone"></div>
  <div class="side-bubble">Lorem Ipsum is simply<br>Lorem Ipsum is simply</div>
  <a class="quote-btn">かんたん見積依頼 <span>›</span></a>
  <h3 class="side-title">Lorem Ipsum</h3>
  <p class="side-text">Lorem Ipsum is simply dummy text of the printing and typesetting industry. Lorem Ipsum has been the industry's standard dummy text ever since</p>
  <ul class="side-menu">
    <li>Lorem Ipsum is simply</li>
    <li class="sub">Lorem Ipsum is simply</li>
    <li class="sub">Lorem Ipsum is simply</li>
    <li class="sub">Lorem Ipsum is simply</li>
    <li class="hot">Lorem Ipsum is simply</li>
    <li>Lorem Ipsum is simply</li>
  </ul>
  <div class="side-card card-feature">
    <div class="visual" role="img" aria-label="Campaign visual with portrait photos of women"></div>
    <p>Lorem Ipsum is simply dummy text of the printing Lorem Ipsum is simply dummy text of the printing</p>
  </div>
  <div class="side-card card-mini"><span class="icon" role="img" aria-label="Small character illustration"></span>Lorem Ipsum is simply</div>
  <div class="side-card card-partner"><b><i></i>Bidlark</b><small>買うときも 売るときも ビッドラーク</small></div>
</aside>

<section class="abs hero">
  <div class="hero-photo" role="img" aria-label="Photo of a smiling shop staff member in a teal shirt"></div>
  <h2 class="hero-title">ブラムタイドスタッフ紹介<br><small>vol.06</small></h2>
  <div class="hero-truck">ブラムタイド</div>
  <div class="hero-rule"></div>
  <div class="hero-badge">スタッフブログ<br>更新中</div>
  <p class="hero-role">ブラムタイド昭島店<br>ショップスタッフ</p>
  <p class="hero-kana">ミタニ ソラ</p>
  <p class="hero-name">三谷 空</p>
  <div class="hero-bubble"><div>買いたい人も！<br>売りたい人も！<br>ぜひ「<b>ブラムの</b><br><b>リサイクルショップ</b>」<br>お立ち寄り下さい</div></div>
  <span class="hero-arrow prev"><svg width="8" height="12" viewBox="0 0 8 12"><path d="M7 1L2 6l5 5" fill="none" stroke="#fff" stroke-width="2.5"/></svg></span>
  <span class="hero-arrow next"><svg width="8" height="12" viewBox="0 0 8 12"><path d="M1 1l5 5-5 5" fill="none" stroke="#fff" stroke-width="2.5"/></svg></span>
  <div class="hero-dots"><i></i><i></i><i></i></div>
</section>

<h2 class="abs ad-heading">Advertisement</h2>
<div class="abs ad ad-discount"><div class="ad-inner">今なら、ネット申込で500円OFF!!<span class="people" role="img" aria-label="Photo of two staff members"></span></div></div>
<div class="abs ad ad-press"><div class="ad-inner">
  <span class="mag" role="img" aria-label="Magazine cover photo"></span>
  <div class="ribbon"><b>ハルノート！</b>に紹介されました！<br><em>4ステップの</em> 簡単時短テク</div>
</div></div>
<div class="abs ad ad-art"><div class="ad-inner" role="img" aria-label="Photo of people working at a landfill site">
  <div class="copy"><b>レン・タバロ<br>ごみアートの奇跡</b><small>ブラムタイドは「レン・タバロ」の<br>スペシャル・パートナーです。</small></div>
</div></div>

<section class="abs news news-left">
  <h3>新着ニュース＆オトクな情報</h3>
  <p class="news-item">Lorem Ipsum is simply dummy text of the printing and typesetting industry. Lorem Ipsum has <a>been the industry's</a></p>
  <p class="news-item">Lorem Ipsum is simply dummy text of the printing and typesetting industry. Lorem Ipsum has <a>been the industry's</a></p>
  <p class="news-item">Lorem Ipsum is simply dummy text of the printing and typesetting industry. Lorem Ipsum has <a>been the industry's</a></p>
</section>
<section class="abs news news-right">
  <h3>ブラムタイドのおすすめサービス</h3>
  <p class="news-item"><strong>Lorem Ipsum is simply dummy</strong>Lorem Ipsum is simply dummy text of the printing and typesetting industry. Lorem Ipsum has <a>been the industry's</a></p>
  <p class="news-item">Lorem Ipsum is simply dummy text of the printing and typesetting industry. Lorem Ipsum has <a>been the industry's</a></p>
  <p class="news-item">Lorem Ipsum is simply dummy text of the printing and typesetting industry. Lorem Ipsum has <a>been the industry's</a></p>
</section>
<div class="abs news-divider"></div>

<section class="abs fb">
  <h3>Find Us On Linkbook</h3>
  <p class="mini-brand">bramtide</p>
</section>

<section class="abs tweets">
  <h3><i></i>Tweets</h3>
  <div class="tweet"><span class="mini-brand">bramtide</span><p>Lorem Ipsum is simply dummy text of the printing and typesetting industry. Lorem Ipsum has been the industry's standard<br><a>http://chirpnest.com/abc.com</a><small>2min ago</small></p></div>
  <div class="tweet alt"><span class="mini-brand">bramtide</span><p>Lorem Ipsum is simply dummy text of the printing and typesetting industry. Lorem Ipsum has been the industry's standard<br><a>http://chirpnest.com/abc.com</a><small>2min ago</small></p></div>
</section>

<section class="abs contact">
  <h3>Lorem Ipsum is simply</h3>
  <a class="btn one">Lorem Ipsum <span>›</span></a>
  <a class="btn two">Lorem Ipsum <span>›</span></a>
  <p class="tel"><svg width="28" height="28" viewBox="0 0 30 30"><circle cx="15" cy="15" r="13" fill="none" stroke="#bbb" stroke-width="2"/><path d="M10 8l3 4-2 2 5 5 2-2 4 3-2 3c-7 0-13-6-13-13z" fill="#bbb"/></svg>0120 418 620</p>
  <p class="hours">9:00am-22.00pm / 9:00am-20:00pm</p>
</section>

<footer class="abs footer">
  <div class="foot-col" style="left:286px"><h4>Lorem Ipsum is simply</h4><ul><li>Lorem Ipsum is simply</li><li>Lorem Ipsum is simply</li><li>Lorem Ipsum is simply</li><li>Lorem Ipsum is simply</li><li>Lorem Ipsum is simply</li></ul></div>
  <div class="foot-col" style="left:516px"><h4>Lorem Ipsum is simply</h4><ul><li>Lorem Ipsum is simply</li><li>Lorem Ipsum is simply</li><li>Lorem Ipsum is simply</li><li>Lorem Ipsum is simply</li><li>Lorem Ipsum is simply</li></ul></div>
  <div class="foot-col" style="left:744px"><h4>Lorem Ipsum is simply</h4><ul><li>Lorem Ipsum is simply</li><li>Lorem Ipsum is simply</li><li>Lorem Ipsum is simply</li><li>Lorem Ipsum is simply</li><li>Lorem Ipsum is simply</li></ul></div>
</footer>

<div class="abs copyright">
  <div class="left"><b>bramtide</b><span>All Right Reserved 2013.</span></div>
  <div class="right">Privacy Policy &nbsp;|&nbsp; Terms &amp; Condition &nbsp;|&nbsp; Contact Us</div>
</div>

</body>
</html>
```